New Look and Feel for 82 year old Varnstedt Ltd. presentations

We are seeking new ideas to have powerpoint-layouts for the group headquarters. Varnstedt is an industrial company in maritime, hydraulics, heavy machinery and industrial services. Please read our history and watch the video for a quick familiarization. http://www.varnstedt-example.fi/eng/main.php

Our customer relationships are based on trust, with Varnstedt providing to customers, cooperation partners and other interest groups products and solutions that produce sustainable benefits.

Varnstedt strives to ensure that the environmental impact of the products is considered over the entire life cycle and the processes used by the Group are as environmentally benign as possible.

Colors

Designer to choose colors to be used in the design.

Requirements
Must have
• Logo
Nice to have
• example animations and transitions

```html
<!DOCTYPE html>
<html lang="en">
<head>
<meta charset="utf-8">
<title>Varnstedt Ltd. – Presentation Look and Feel</title>
<link href="https://fonts.googleapis.com/css2?family=Montserrat:wght@400;500;600;700&family=Open+Sans:wght@400;600;700&display=swap" rel="stylesheet">
<style>
:root{
  --red:#e8403f;
  --dark:#3b3b3e;
  --darker:#2a2a2c;
  --grey:#6d6d70;
  --light:#f2f3f5;
  --text:#4a4a4a;
  --muted:#9a9a9a;
  --white:#ffffff;
}
*{box-sizing:border-box;margin:0;padding:0}
html,body{width:957px;height:1200px;overflow:hidden;background:var(--white)}
body{position:relative;font-family:"Open Sans",sans-serif;color:var(--text)}
.slide{position:absolute;width:312px;height:234px;overflow:hidden;background:var(--white);box-shadow:0 0 3px rgba(0,0,0,.25)}
.c1{left:3px}.c2{left:322px}.c3{left:640px}
.r1{top:3px}.r2{top:242px}.r3{top:481px}.r4{top:720px}.r5{top:959px}
.title{position:absolute;left:17px;top:16px;font-family:"Montserrat",sans-serif;font-weight:500;font-size:14px;color:var(--dark)}
.title::after{content:"";display:block;width:26px;height:2px;background:var(--red);margin-top:5px}
.title.light{color:var(--white)}
.brand{position:absolute;right:10px;top:12px;display:flex;align-items:center;gap:3px;font-family:"Montserrat",sans-serif;font-weight:700;font-size:7px;color:var(--dark)}
.brand i{display:block;width:7px;height:7px;background:var(--red)}
.footer{position:absolute;left:0;right:0;bottom:4px;height:6px;border-top:2px solid var(--dark);border-bottom:2px solid var(--red)}
.footer i{position:absolute;left:50%;top:-5px;width:8px;height:10px;margin-left:-4px;background:var(--red)}
.footer.ondark{border-top-color:var(--muted)}
.foot-note{position:absolute;right:10px;bottom:13px;font-size:3px;color:var(--muted)}
.small{font-size:4px;line-height:1.45;color:var(--muted)}
.photo{position:absolute}
.abs{position:absolute}
/* cover slides */
.cover-band{position:absolute;left:0;right:0;top:115px;height:30px;background:var(--darker)}
.cover-mark{position:absolute;left:52px;top:112px;height:36px;padding:0 6px;display:flex;align-items:center;gap:4px;background:var(--white);font-family:"Montserrat",sans-serif;font-weight:700;font-size:11px;color:var(--dark)}
.cover-mark i{width:11px;height:11px;background:var(--red);display:block}
.cover-title{position:absolute;font-family:"Montserrat",sans-serif;font-weight:500}
/* agenda */
.agenda{position:absolute;display:flex;gap:6px;width:120px}
.agenda .dot{flex:none;width:13px;height:13px;border-radius:50%;background:var(--dark)}
.agenda.hot .dot{background:var(--red)}
.agenda h4{font-weight:400;font-size:6px;color:var(--text)}
.agenda.hot h4{color:var(--red)}
/* icon slide */
.icon-row{position:absolute;display:flex;gap:8px;width:112px}
.icon-row .dot{flex:none;width:20px;height:20px;border-radius:50%;background:var(--dark);border:2px solid #ddd}
.icon-row.hot .dot{background:var(--red);border-color:rgba(255,255,255,.3)}
.icon-row h5{font-size:4.5px;font-weight:700;color:var(--dark)}
.icon-row.hot h5{color:var(--white)}
.icon-row.hot .small{color:#ddd}
/* portfolio */
.badge{position:absolute;border:1.5px solid var(--grey)}
</style>
</head>
<body>

<!-- 1 cover light -->
<section class="slide c1 r1">
  <div class="photo" role="img" aria-label="Pale industrial machinery photograph" style="inset:0;background:linear-gradient(120deg,#eef0f4,#dfe3ea 50%,#f4f5f7)"></div>
  <div class="cover-band"></div>
  <div class="cover-mark"><i></i>Varnstedt</div>
  <h1 class="cover-title" style="left:53px;top:156px;font-size:16px;color:var(--dark)">Your Title Goes Here</h1>
  <p class="abs" style="left:54px;top:178px;font-size:6px;font-weight:600;color:var(--red)">Your Subtitle Goes Here</p>
</section>

<!-- 2 cover dark -->
<section class="slide c2 r1" style="background:var(--darker)">
  <div class="photo" role="img" aria-label="Dark close-up of heavy machinery with hoses" style="inset:0;background:radial-gradient(circle at 70% 45%,#4a4a4a,#1f1f20 70%)"></div>
  <div class="abs" style="left:80px;top:0;width:27px;height:234px;background:rgba(232,64,63,.75)"></div>
  <div class="abs" style="left:33px;top:110px;display:flex;align-items:center;gap:3px;font-family:Montserrat,sans-serif;font-weight:700;font-size:10px;color:var(--white)"><i style="display:block;width:9px;height:9px;background:var(--red)"></i>Varnstedt</div>
  <h1 class="cover-title" style="left:97px;top:108px;font-size:18px;color:var(--white)">Your Title Goes Here</h1>
  <p class="abs" style="left:98px;top:134px;font-size:6.5px;font-weight:600;color:var(--white)">Your Subtitle Goes Here</p>
</section>

<!-- 3 agenda -->
<section class="slide c3 r1">
  <h2 class="title">Our Agenda</h2>
  <div class="brand"><i></i>Varnstedt</div>
  <div class="agenda" style="left:42px;top:52px"><span class="dot"></span><div><h4>Agenda One</h4><p class="small">10:00 · Short note on this topic and its main goals for today.</p></div></div>
  <div class="agenda hot" style="left:42px;top:104px"><span class="dot"></span><div><h4>Agenda Two</h4><p class="small">11:00 · Short note on this topic and its main goals for today.</p></div></div>
  <div class="agenda" style="left:42px;top:150px"><span class="dot"></span><div><h4>Agenda Three</h4><p class="small">12:00 · Short note on this topic and its main goals for today.</p></div></div>
  <div class="agenda" style="left:180px;top:52px"><span class="dot"></span><div><h4>Agenda Four</h4><p class="small">13:00 · Short note on this topic and its main goals for today.</p></div></div>
  <div class="agenda hot" style="left:180px;top:101px"><span class="dot"></span><div><h4>Agenda Five</h4><p class="small">14:00 · Short note on this topic and its main goals for today.</p></div></div>
  <div class="agenda" style="left:180px;top:150px"><span class="dot"></span><div><h4>Agenda Six</h4><p class="small">15:00 · Short note on this topic and its main goals for today.</p></div></div>
  <p class="foot-note">© Varnstedt Ltd.</p>
  <div class="footer"><i></i></div>
</section>

<!-- 4 title image text -->
<section class="slide c1 r2">
  <h2 class="title">Title And Image + Text</h2>
  <div class="brand"><i></i>Varnstedt</div>
  <div class="photo" role="img" aria-label="Green valve on dark machinery" style="left:22px;top:48px;width:150px;height:82px;background:linear-gradient(90deg,#1d2a22,#3d5a3a 40%,#2b2b2b)"></div>
  <div class="abs" style="left:172px;top:48px;width:128px;height:82px;background:#3e3e3e;display:flex;align-items:center;justify-content:center;gap:5px;font-family:Montserrat,sans-serif;font-weight:700;font-size:15px;color:var(--white)"><i style="display:block;width:14px;height:14px;background:var(--red)"></i>Varnstedt</div>
  <p class="abs" style="left:25px;top:138px;width:110px;font-size:6.5px;line-height:1.35;color:var(--text)">Lorem ipsum dolor sit amet, consectetur adipiscing elit, sed do eiusmod tempor incididunt ut labore et dolore magna aliqua. Ut enimad minim veniam, quis</p>
  <p class="abs small" style="left:160px;top:138px;width:138px">Our teams deliver reliable service across maritime and hydraulic projects, with care for every detail and lasting value for each customer.</p>
  <p class="abs small" style="left:160px;top:166px;width:138px">We plan for the full product life cycle and keep our work processes as clean and safe as possible.</p>
  <div class="footer"><i></i></div>
</section>

<!-- 5 icon slide -->
<section class="slide c2 r2">
  <h2 class="title">Icon Slide</h2>
  <div class="photo" role="img" aria-label="Dark rusty machine part" style="left:161px;top:0;width:151px;height:234px;background:linear-gradient(160deg,#3a3330,#1f1f20 60%,#4b4644)"></div>
  <div class="icon-row" style="left:33px;top:43px"><span class="dot"></span><div><h5>STRATEGY</h5><p class="small">Clear goals guide our long term growth in every market.</p></div></div>
  <div class="icon-row" style="left:33px;top:112px"><span class="dot"></span><div><h5>MARKETING</h5><p class="small">We share our story with partners and customers alike.</p></div></div>
  <div class="icon-row" style="left:33px;top:181px"><span class="dot"></span><div><h5>MARKETING</h5><p class="small">We share our story with partners and customers alike.</p></div></div>
  <div class="icon-row hot" style="left:151px;top:43px"><span class="dot"></span><div><h5>STRATEGY</h5><p class="small">Clear goals guide our long term growth in every market.</p></div></div>
  <div class="icon-row hot" style="left:151px;top:112px"><span class="dot"></span><div><h5>MARKETING</h5><p class="small">We share our story with partners and customers alike.</p></div></div>
  <div class="icon-row hot" style="left:151px;top:181px"><span class="dot"></span><div><h5>STRATEGY</h5><p class="small">Clear goals guide our long term growth in every market.</p></div></div>
  <div class="footer"><i></i></div>
</section>

<!-- 6 title image strip -->
<section class="slide c3 r2">
  <h2 class="title">Your Title Here</h2>
  <div class="brand"><i></i>Varnstedt</div>
  <div class="photo" role="img" aria-label="Yellow and black hydraulic hoses" style="left:0;top:67px;width:94px;height:100px;background:linear-gradient(180deg,#6b6440,#2e3136)"></div>
  <div class="abs" style="left:94px;top:67px;width:125px;height:100px;background:#4a4542;color:var(--white);text-align:center">
    <svg width="14" height="12" viewBox="0 0 14 12" style="margin-top:26px"><path d="M7 11 1.5 5.5A3 3 0 0 1 7 2a3 3 0 0 1 5.5 3.5Z" fill="none" stroke="#fff" stroke-width="1"/></svg>
    <p style="font-size:6px">Welcome</p>
    <p class="small" style="color:#ccc;padding:2px 20px">Short welcome line for our guests and partners today.</p>
  </div>
  <div class="photo" role="img" aria-label="Close-up of heavy hydraulic pipes" style="left:219px;top:67px;width:93px;height:100px;background:linear-gradient(180deg,#7d7650,#3a4a5a)"></div>
  <div class="footer"><i></i></div>
</section>

<!-- 7 about us photo -->
<section class="slide c1 r3">
  <div class="photo" role="img" aria-label="Worker in blue helmet and safety harness" style="inset:0;background:linear-gradient(100deg,#e7ebf0 0,#c9d2de 30%,#4a6a9a 55%,#2f3d5c)"></div>
  <div class="brand"><i></i>Varnstedt</div>
  <div class="abs" style="left:157px;top:65px;width:155px;height:112px;background:rgba(59,59,62,.92);padding:10px 10px">
    <h2 style="font-family:Montserrat,sans-serif;font-weight:500;font-size:14px;color:var(--white);margin-bottom:8px">About Us</h2>
    <p class="small" style="color:#e5e5e5">For decades our people have built and serviced heavy machinery for ports, ships and plants, earning trust through quality work.</p>
    <p class="small" style="color:#e5e5e5;margin-top:5px">We keep the environmental impact of our products in view over their whole life cycle.</p>
  </div>
  <div class="footer"><i></i></div>
</section>

<!-- 8 about us dark -->
<section class="slide c2 r3" style="background:var(--dark)">
  <h2 class="title light">About Us</h2>
  <div class="photo" role="img" aria-label="Portrait of a team member" style="left:119px;top:50px;width:74px;height:74px;border-radius:50%;background:radial-gradient(circle,#c9b8a8,#6c7a8c);border:2px solid #fff"></div>
  <p class="abs small" style="left:28px;top:138px;width:256px;text-align:center;color:#ddd">Our team works closely with customers and partners to create solutions that bring lasting benefits to every project we take on.</p>
  <p class="abs small" style="left:28px;top:155px;width:256px;text-align:center;color:#ddd">We value open cooperation, safe work and a careful use of resources.</p>
  <div class="abs" style="left:135px;top:191px;display:flex;gap:9px"><span style="width:8px;height:8px;border-radius:50%;border:1px solid #fff"></span><span style="width:8px;height:8px;border-radius:50%;border:1px solid #fff"></span><span style="width:8px;height:8px;border-radius:50%;border:1px solid #fff"></span></div>
</section>

<!-- 9 video -->
<section class="slide c3 r3">
  <h2 class="title" style="top:44px;width:80px;line-height:1.2">Your Title Goes Here</h2>
  <div class="abs" style="left:17px;top:92px;width:80px">
    <p class="small">Short text about the video and what it shows to our viewers.</p>
    <p class="small" style="margin-top:5px">Watch our crew at work in the main hall.</p>
    <p class="small" style="margin-top:5px">Clip length is about two minutes.</p>
  </div>
  <div class="abs" style="left:112px;top:45px;width:190px;height:137px;background:#d9dadc;border-radius:4px;padding:5px">
    <div class="photo" role="img" aria-label="Video still of a technician at a workbench" style="position:relative;width:100%;height:113px;background:linear-gradient(135deg,#5a5a5c,#2a2a2c 60%,#6a4a3a)"></div>
    <span class="abs" style="left:88px;top:50px;width:16px;height:16px;border-radius:50%;background:var(--red)"></span>
  </div>
  <div class="abs" style="left:197px;top:182px;width:20px;height:10px;background:#cfcfd1"></div>
  <div class="abs" style="left:180px;top:191px;width:54px;height:2px;background:#bfbfc1"></div>
  <div class="footer"><i></i></div>
</section>

<!-- 10 section break -->
<section class="slide c1 r4" style="background:var(--dark)">
  <div class="abs" style="left:0;right:0;top:141px;height:20px;background:var(--red)"></div>
  <div class="abs" style="left:30px;top:141px;width:95px;height:20px;background:var(--dark);display:flex;align-items:center;justify-content:center;gap:3px;font-family:Montserrat,sans-serif;font-weight:700;font-size:9px;color:var(--white)"><i style="display:block;width:8px;height:8px;background:var(--red)"></i>Varnstedt</div>
  <h2 class="abs" style="left:26px;top:171px;font-family:Montserrat,sans-serif;font-weight:600;font-size:14px;color:var(--white)">Section Break</h2>
  <p class="abs" style="left:26px;top:189px;width:160px;font-size:4.5px;line-height:1.4;color:#e0e0e0">Short intro line for the next part of this talk on our work and our goals for the year ahead.</p>
</section>

<!-- 11 title image quote -->
<section class="slide c2 r4">
  <h2 class="title">Title And Image + Text</h2>
  <div class="brand"><i></i>Varnstedt</div>
  <div class="photo" role="img" aria-label="Sparks flying from grinding work on a large ring" style="left:17px;top:46px;width:140px;height:84px;background:linear-gradient(135deg,#2a2420,#7a5a30 40%,#3a3e4a)"></div>
  <div class="abs" style="left:157px;top:46px;width:138px;height:84px;background:var(--dark);padding:12px 16px;color:var(--white)">
    <p style="font-size:5px;line-height:1.45">“ Great work starts with people who care about every part, from design to daily service on site. ”</p>
    <p style="font-size:4px;color:#bbb;margin-top:5px">– Aino Lehto –</p>
  </div>
  <div class="abs" style="left:20px;top:138px;width:275px">
    <p class="small">We build, repair and maintain machines for ports, ships and plants. Each job is planned with care so customers get safe, lasting results every day.</p>
    <p class="small" style="margin-top:3px">Our teams work side by side with partners and share knowledge openly across the group.</p>
    <p class="small" style="margin-top:3px">We look at the full life cycle of our products and keep our processes clean and efficient.</p>
    <p class="small" style="margin-top:3px">Talk to us about your next project and how we can help you grow.</p>
  </div>
  <div class="footer"><i></i></div>
</section>

<!-- 12 about us panel -->
<section class="slide c3 r4">
  <div class="abs" style="left:173px;top:0;width:139px;height:234px;background:var(--grey)"></div>
  <h2 class="title">About Us</h2>
  <div class="photo" role="img" aria-label="Worker beside a large ship propeller" style="left:26px;top:55px;width:130px;height:89px;background:linear-gradient(135deg,#8a7a6a,#4a3a30 50%,#c8b8a8)"></div>
  <p class="abs small" style="left:20px;top:152px;width:142px;text-align:center">We serve maritime, hydraulic and heavy industry clients with skilled teams and modern tools. Our aim is steady quality, fair prices and lasting customer trust in each market we serve.</p>
  <p class="abs" style="left:188px;top:86px;width:105px;font-size:4.5px;line-height:1.45;color:var(--white);background:rgba(255,255,255,.12)">Who are we? A group of skilled makers and service teams. We build, fix and care for heavy machines across many fields, and we keep our word with every client we serve.</p>
</section>

<!-- 13 company details -->
<section class="slide c1 r5">
  <h2 class="title">Company Details</h2>
  <div class="brand"><i></i>Varnstedt</div>
  <div class="abs" style="left:22px;top:65px;width:120px">
    <p style="font-size:4.5px;font-weight:700;color:var(--dark)">Short headline for this company overview</p>
    <p class="small">Founded long ago, we now serve clients in many lands with a broad range of services.</p>
    <p class="small" style="margin-top:8px">✓ Maritime repair and new builds for ports</p>
    <p class="small" style="margin-top:5px">✓ Hydraulic systems built to order</p>
    <p class="small" style="margin-top:5px">✓ Heavy machinery service on site</p>
    <p class="small" style="margin-top:5px">✓ Industrial maintenance contracts</p>
  </div>
  <div class="abs" style="left:166px;top:65px;width:130px;height:101px;background:var(--red);display:flex;align-items:center;justify-content:center;gap:5px;font-family:Montserrat,sans-serif;font-weight:700;font-size:16px;color:var(--dark)"><i style="display:block;width:14px;height:14px;background:var(--dark)"></i>Varnstedt</div>
  <p class="foot-note">© Varnstedt Ltd.</p>
  <div class="footer"><i></i></div>
</section>

<!-- 14 blank -->
<section class="slide c2 r5">
  <h2 class="title">Your Blank Slide</h2>
  <div class="brand"><i></i>Varnstedt</div>
  <p class="foot-note">© Varnstedt Ltd.</p>
  <div class="footer"><i></i></div>
</section>

<!-- 15 portfolio -->
<section class="slide c3 r5">
  <div class="badge" role="img" aria-label="Label design sample" style="left:16px;top:26px;width:56px;height:28px;border-radius:2px"></div>
  <div class="badge" role="img" aria-label="Label design sample" style="left:88px;top:26px;width:62px;height:28px;border-radius:14px"></div>
  <div class="badge" role="img" aria-label="Label design sample" style="left:166px;top:26px;width:62px;height:28px"></div>
  <div class="badge" role="img" aria-label="Label design sample" style="left:244px;top:22px;width:52px;height:36px;border-radius:50%"></div>
  <div class="badge" role="img" aria-label="Label design sample" style="left:10px;top:103px;width:62px;height:24px"></div>
  <div class="abs" style="left:78px;top:78px;width:156px;height:77px;background:var(--dark);display:flex;align-items:center;justify-content:center;font-family:Montserrat,sans-serif;font-weight:600;font-size:17px;color:var(--white)">Our Portfolio</div>
  <div class="badge" role="img" aria-label="Round label design sample" style="left:248px;top:90px;width:52px;height:52px;border-radius:50%"></div>
  <div class="badge" role="img" aria-label="Label design sample" style="left:10px;top:176px;width:62px;height:36px"></div>
  <div class="badge" role="img" aria-label="Label design sample" style="left:90px;top:176px;width:56px;height:36px;border-radius:3px"></div>
  <div class="badge" role="img" aria-label="Label design sample" style="left:166px;top:176px;width:64px;height:36px;border-radius:18px 18px 3px 3px"></div>
  <div class="badge" role="img" aria-label="Label design sample" style="left:246px;top:178px;width:52px;height:32px;border-radius:50%"></div>
</section>

</body>
</html>
```